Veteran Owned General Contractor needs Bold New Business Cards

We are a service disabled veteran owned small business. We're a general contractor that specializes in excavation, underground utilities, site work, land clearing and demolition. We would like a fresh, simple, bold, new look for our business cards. We're open to ideas! We'd like to incorporate the following information on the card:

Company Name & Logo, Name of Person, Job Title, Office Phone, Fax, Cell Phone, Email Address, Website, SDVOSB

Our logo is included. We look forward to your thoughts.

Thank you!
Updates

Reason: Hello Due to the overwhelming response to this project, we are extending the deadline one time to allow for improved communication and feedback with the top candidates. We would like to thank everyone for their hard work and exceptional creativity! Thank you

Industry/Entity Type

Business

Contact Information for Business Card

Font styles to use
Sans Serif

Requirements
Nice to have
• As we are a veteran owned company, it would be nice to incorporate an American flag into the design. Maybe on the back?

```html
<!DOCTYPE html>
<html lang="en">
<head>
<meta charset="utf-8">
<title>Valdrent Business Card</title>
<link rel="stylesheet" href="https://fonts.googleapis.com/css2?family=Open+Sans:wght@300;400;700;800&display=swap">
<style>
  :root {
    --backdrop: #e9e8e5;
    --card-black: #1c1c1c;
    --card-black-soft: #2a2a2a;
    --card-white: #ffffff;
    --brand-green: #6cc04a;
    --name-grey: #555555;
    --title-blue: #3a9ad9;
    --text-light: #e6e6e6;
    --text-muted: #8a8a8a;
    --mark-grey: #7d7d7d;
  }
  * { margin: 0; padding: 0; box-sizing: border-box; }
  html, body {
    width: 1200px; height: 804px; overflow: hidden;
    background: var(--backdrop);
    font-family: "Open Sans", sans-serif;
  }
  .canvas {
    position: relative; width: 1200px; height: 804px;
    display: flex; align-items: center; justify-content: center; gap: 80px;
  }
  .card {
    position: relative; width: 500px; height: 290px;
    border-radius: 18px; overflow: hidden;
    box-shadow: 0 10px 28px rgba(0,0,0,0.22);
  }

  /* Back of card */
  .card-back {
    background: linear-gradient(160deg, var(--card-black-soft) 0%, var(--card-black) 55%, #111 100%);
    display: flex; flex-direction: column; align-items: center; justify-content: center;
  }
  .brand {
    display: flex; align-items: center; gap: 12px;
    color: var(--brand-green); font-weight: 800; letter-spacing: 1px;
    white-space: nowrap;
  }
  .brand-square { background: var(--mark-grey); flex: none; }
  .card-back .brand { font-size: 38px; }
  .card-back .brand-square { width: 34px; height: 34px; }
  .website {
    margin-top: 22px; color: var(--text-muted);
    font-size: 12px; letter-spacing: 0.5px;
  }

  /* Front of card */
  .card-front { background: var(--card-white); }
  .front-top {
    position: absolute; left: 0; top: 0; width: 100%; height: 150px;
  }
  .holder {
    position: absolute; left: 36px; bottom: 14px;
  }
  .holder-name {
    font-size: 24px; font-weight: 300; color: var(--name-grey); letter-spacing: 1px;
  }
  .holder-title {
    font-size: 13px; color: var(--title-blue); margin-top: 2px; margin-left: 40px;
  }
  .front-top .brand {
    position: absolute; right: 40px; top: 58px; font-size: 28px; gap: 8px;
  }
  .front-top .brand-square { width: 24px; height: 24px; }
  .front-bottom {
    position: absolute; left: 0; top: 150px; width: 100%; height: 140px;
    background: linear-gradient(170deg, var(--card-black-soft) 0%, var(--card-black) 60%, #111 100%);
    display: flex; align-items: center; padding: 0 30px;
    color: var(--text-light); font-size: 12.5px; line-height: 1.55;
  }
  .contact-main { width: 200px; white-space: nowrap; }
  .divider {
    width: 0; height: 44px; border-left: 2px dotted var(--text-light);
    margin: 0 26px 0 12px;
  }
  .contact-extra { flex: 1; white-space: nowrap; }
  .address { display: flex; gap: 6px; align-items: flex-start; }
  .pin-icon { width: 10px; height: 13px; margin-top: 3px; flex: none; }
</style>
</head>
<body>
<main class="canvas">
  <section class="card card-back" aria-label="Card back">
    <div class="brand"><span class="brand-square"></span><span class="brand-name">VALDRENT</span></div>
    <p class="website">www.valdrentsite.com.au</p>
  </section>

  <section class="card card-front" aria-label="Card front">
    <div class="front-top">
      <div class="holder">
        <p class="holder-name">YOUR NAME</p>
        <p class="holder-title">Designation</p>
      </div>
      <div class="brand"><span class="brand-square"></span><span class="brand-name">VALDRENT</span></div>
    </div>
    <div class="front-bottom">
      <div class="contact-main">
        <p>+1-(123)-456-7890</p>
        <p>+1-(123)-456-7890</p>
        <p>hello@valdrentsite.com</p>
      </div>
      <div class="divider"></div>
      <div class="contact-extra">
        <p>Fax &nbsp;+1-(123)-456-7890</p>
        <p class="address">
          <svg class="pin-icon" viewBox="0 0 10 13" aria-hidden="true">
            <path d="M5 0a5 5 0 0 0-5 5c0 3.5 5 8 5 8s5-4.5 5-8a5 5 0 0 0-5-5zm0 7a2 2 0 1 1 0-4 2 2 0 0 1 0 4z" fill="#e6e6e6"/>
          </svg>
          <span>Lorem Ipsum is simply<br>dummy text of the printing</span>
        </p>
      </div>
    </div>
  </section>
</main>
</body>
</html>
```